Bref créative
Bath/Spa Product Label
Vesta Reef
Thanks to you expert graphic artists we have been happy with the logo designed last summer and would like to see what you wizards can do to with a product label.
We have attached the current logo and would love to see what you can do with creating a product label that will fit several types of labels.
1. We need a vertical orientation of the label to be scalable so that we can use it on 16 oz or 8 ounce bottles.
2. We need a horizontal orientation that is also scalable for 8 ounce or 4 ounce jars.
You can place the uploaded logo anywhere on the labels but we need blank space to fill in the product name, net weight, instructions and ingredients.
Feel free to apply generic text for the net weight, instructions and ingredients. We manufacture shampoos, conditioners, body washes, shower gels, body scrubs, foot scrubs, sugar scrubs, etc.
We have attached two sample MS Word documents with the ugly and boring labels we use now. Use these as inspiration to move us to the next level. Go ahead add color, fonts, additional graphics - whatever you see fit. In the past, we have treated our designers fairly and cordially. You can expect the same treatment for this contest.
Personal Care
Over 95% of our customer base is women. But keep in mind that men also use shower gels - so no teddy bears on the product label please.Our clients are used to high quality product, not over hyped claims or garish designs.
As stated above we need the label in at least two orientations. It must also be scalable so that we can use it on different size labels. If you can design a third label in square dimensions that would be a big bonus.
Current jar label - for example DO NOT REPLICATE.
Sample shampoo/body wash label applied vertically to 16 ounce or 8 ounce bottles. FOR EXAMPLE ONLY DO NOT REPLICATE
Current logo - DO NOT DISTRIBUTE - COPYRIGHT VESTA REEF.

```html
<!DOCTYPE html>
<html lang="en">
<head>
<meta charset="utf-8">
<title>Vesta Reef Product Labels</title>
<link href="https://fonts.googleapis.com/css2?family=Cinzel:wght@400;600&family=Arimo:wght@400;700&display=swap" rel="stylesheet">
<style>
:root{
  --teal:#1a9a8a;
  --teal-dark:#0f7d70;
  --gold:#d8b14e;
  --gold-light:#f1dc9a;
  --cream:#fbf3dd;
  --blue:#2a3a8c;
  --blue-light:#5a68b6;
  --lilac:#c9c3e6;
  --purple:#7a3a96;
  --purple-light:#c7a6d8;
  --ink:#3a3a3a;
  --white:#ffffff;
}
*{box-sizing:border-box;margin:0;padding:0}
html,body{width:1200px;height:727px;overflow:hidden;background:var(--white)}
body{position:relative;font-family:"Arimo",Arial,sans-serif;color:var(--ink)}
.label{position:absolute;overflow:hidden;border:1px solid #ddd;background:var(--white)}
.brand{font-family:"Cinzel",Georgia,serif;font-weight:600;letter-spacing:2px;text-align:center;white-space:nowrap}
.brand-dot{display:block;margin:0 auto 6px;border-radius:50%;background:var(--gold)}
.fine{font-size:7px;line-height:1.35}

/* Jar label */
.jar{left:84px;top:72px;width:679px;height:144px}
.jar-side{position:absolute;top:0;width:108px;height:144px;background:linear-gradient(180deg,var(--cream),var(--gold-light) 70%)}
.jar-side .art{position:absolute;left:0;top:0;width:108px;height:110px;background:radial-gradient(ellipse at 50% 75%,var(--gold) 0,var(--gold-light) 45%,transparent 70%)}
.jar-side .bar{position:absolute;left:0;bottom:0;width:108px;height:34px;background:var(--teal);color:var(--white);font-size:10px;font-weight:700;padding:11px 0 0 8px}
.jar-side.left{left:0}
.jar-side.right{left:408px}
.jar-front{position:absolute;left:108px;top:0;width:300px;height:144px;background:radial-gradient(ellipse at 50% 45%,var(--white) 40%,var(--cream) 75%,var(--gold-light))}
.jar-front .brand-dot{width:16px;height:16px;margin-top:28px}
.jar-front .brand{font-size:22px;color:var(--teal)}
.jar-front .product{position:absolute;left:40px;right:40px;top:112px;height:20px;background:var(--teal);color:var(--white);font-size:11px;text-align:center;line-height:20px;letter-spacing:.5px}
.jar-info{position:absolute;left:524px;top:22px;width:148px;color:var(--teal)}
.jar-info p+p{margin-top:8px}

/* Sugar scrub label */
.scrub{left:413px;top:278px;width:348px;height:351px}
.scrub-top{position:absolute;left:0;top:0;width:348px;height:218px;background:linear-gradient(180deg,var(--cream),var(--white) 35%,var(--white) 55%,var(--lilac))}
.scrub .brand-dot{width:20px;height:20px;margin-top:22px}
.scrub .brand{font-size:26px;color:var(--teal)}
.scrub .art{position:absolute;left:90px;top:110px;width:168px;height:108px;border-radius:84px 84px 0 0;background:linear-gradient(180deg,var(--gold-light),var(--gold))}
.scrub-band{position:absolute;left:0;top:218px;width:348px;height:44px;background:linear-gradient(180deg,var(--blue),var(--blue-light));color:var(--white);text-align:center}
.scrub-band h2{font-size:15px;font-weight:400;letter-spacing:.5px;margin-top:5px}
.scrub-band p{font-size:12px;margin-top:2px}
.scrub-weight{position:absolute;left:0;top:265px;width:348px;text-align:center;font-size:9px;color:var(--blue)}
.scrub-info{position:absolute;left:18px;top:288px;width:312px;color:var(--blue)}

/* Conditioner label */
.bottle{left:792px;top:67px;width:379px;height:562px}
.bottle-main{position:absolute;left:0;top:0;width:336px;height:562px;background:linear-gradient(180deg,var(--white) 30%,var(--purple-light) 55%,var(--purple))}
.bottle .art{position:absolute;left:0;top:190px;width:336px;height:372px;background:radial-gradient(circle at 80% 35%,rgba(255,255,255,.35),transparent 45%),radial-gradient(ellipse at 45% 80%,rgba(216,177,78,.55),transparent 40%)}
.bottle .brand-dot{width:26px;height:26px;margin-top:40px}
.bottle .brand{font-size:30px;color:var(--teal)}
.bottle-name{position:absolute;left:32px;right:32px;top:440px;height:28px;border-radius:6px;background:var(--lilac);color:var(--purple);font-size:17px;text-align:center;line-height:28px;letter-spacing:.5px}
.bottle-desc{position:absolute;left:0;width:336px;top:476px;text-align:center;color:var(--white);font-size:15px}
.bottle-weight{position:absolute;left:0;width:336px;top:530px;text-align:center;color:var(--white);font-size:10px}
.bottle-info{position:absolute;left:336px;top:0;width:43px;height:562px;background:var(--white)}
.bottle-info p{position:absolute;left:50%;top:50%;width:540px;transform:translate(-50%,-50%) rotate(90deg);color:var(--purple);font-size:7px;line-height:1.35}
</style>
</head>
<body>

<section class="label jar" aria-label="Jar label">
  <div class="jar-side left">
    <div class="art" role="img" aria-label="Golden shell illustration"></div>
    <div class="bar">NET WT. 8oz.</div>
  </div>
  <div class="jar-front">
    <span class="brand-dot"></span>
    <div class="brand">VESTA REEF</div>
    <div class="product">BODY CREAM AND DESCRIPTION</div>
  </div>
  <div class="jar-side right">
    <div class="art" role="img" aria-label="Golden shell illustration"></div>
    <div class="bar"></div>
  </div>
  <div class="jar-info fine">
    <p>INGREDIENTS: Sucrose, Carthamus tinctorius (Safflower) Seed Oil, Polysorbate 80, Tocopherol Acetate (Vitamin E), Fragrance, Mica, Phenoxyethanol</p>
    <p>WARNING: This product contains natural oils that can make surfaces slippery. Use caution whenever using this product to prevent possible injury.</p>
  </div>
</section>

<section class="label scrub" aria-label="Sugar scrub label">
  <div class="scrub-top">
    <span class="brand-dot"></span>
    <div class="brand">VESTA REEF</div>
    <div class="art" role="img" aria-label="Golden shell with soft bubbles"></div>
  </div>
  <div class="scrub-band">
    <h2>GLISTENING SUGAR SCRUB</h2>
    <p>with Jojoba Beads and Lavender Mint Scent</p>
  </div>
  <div class="scrub-weight">NET WT. 8oz.</div>
  <div class="scrub-info fine">
    <p>INGREDIENTS: Sucrose, Carthamus tinctorius (Safflower) Seed Oil, Polysorbate 80, Tocopherol Acetate (Vitamin E), Fragrance, Mica, Phenoxyethanol</p>
    <p>WARNING: This product contains natural oils that can make surfaces slippery. Use caution whenever using this product to prevent possible injury.</p>
  </div>
</section>

<section class="label bottle" aria-label="Bottle label">
  <div class="bottle-main">
    <div class="art" role="img" aria-label="Purple swirl pattern with golden shell"></div>
    <span class="brand-dot"></span>
    <div class="brand">VESTA REEF</div>
    <div class="bottle-name">CONDITIONER</div>
    <div class="bottle-desc">Description of Product</div>
    <div class="bottle-weight">NET WT. 8oz.</div>
  </div>
  <div class="bottle-info">
    <p>DIRECTIONS: Apply to clean damp hair, work through to the ends and rinse well. INGREDIENTS: Water, Cetyl Alcohol, Glycerin, Panthenol, Fragrance, Phenoxyethanol. WARNING: Avoid contact with eyes. Use caution in wet areas to prevent possible injury.</p>
  </div>
</section>

</body>
</html>
```